Design a label for a range of honey under :BRIGHT MEADOW HONEY. (Original quirky different)

Create a label for a range of honey products under the brand BRIGHT MEADOW HONEY.
Iam the beekeeper and want to sell for the local New Zealand market directly to the consumer, online mainly.
Brand position: A contemporary honey, a fresh look for a simple product, like nature intended, nothing taken out, nothing added. Doesnt take itself seriously.
Personality: Contemporary, fresh, modern, free and fun,loving. Doesnt take itself seriously, loving, generous, upbeat, provide enjoyment, life ...
Brand value: Straight up, keep it simple, generous, different,
Label: Modern twist of nature and goodness (no straight picture of nature) quirky?, use of slogan? ( Nature in a pot / More than just honey / Taste of nature / It's all good...
Need to stand out, make you smile, be noticed, different...

Target Market(s)

Online direct customer.

Requirements
Must have
• legal requirements for NZ labeling attached.
A twist and quirky side...
Should not have
• Basic picture of nature.
Straight forward boring everybody else's feel.

```html
<!DOCTYPE html>
<html lang="en">
<head>
<meta charset="utf-8">
<title>Bright Meadow Honey – Organic Honey Label</title>
<link href="https://fonts.googleapis.com/css2?family=Bodoni+Moda:wght@500;600;700&family=Montserrat:wght@400;500&display=swap" rel="stylesheet">
<style>
  :root {
    --honey-cream: #fde598;
    --honey-light: #fff1c2;
    --comb-gap: #ffffff;
    --bark: #4a1a0c;
    --stage: #f3f0e9;
    --panel-white: #ffffff;
    --rule: #8a5a48;
  }
  * { margin: 0; padding: 0; box-sizing: border-box; }
  html, body {
    width: 1200px; height: 1200px; overflow: hidden;
    background: var(--stage);
  }
  .label {
    position: absolute; left: 40px; top: 413px;
    width: 936px; height: 312px;
    transform: scale(1.1966); transform-origin: top left;
    background: var(--comb-gap);
    color: var(--bark);
    font-family: "Bodoni Moda", "Times New Roman", serif;
    font-variant-numeric: lining-nums;
  }
  .label-shapes { position: absolute; inset: 0; width: 936px; height: 312px; }
  .label-shapes .panel { fill: var(--honey-cream); }
  .label-shapes .comb-area { fill: url(#combTone); }

  .center-text {
    position: absolute; left: 306px; width: 327px;
    text-align: center; line-height: 1;
  }
  .net-weight { top: 13px; font-size: 11px; font-weight: 600; letter-spacing: 1.5px; }
  .brand-name {
    top: 70px; font-size: 19px; font-weight: 700; letter-spacing: 1px; line-height: 1.1;
  }
  .product-type { top: 180px; font-size: 13px; font-weight: 500; letter-spacing: 2px; }
  .product-name { top: 194px; font-size: 29px; font-weight: 700; letter-spacing: 5px; }
  .company { top: 262px; font-size: 10px; font-weight: 600; letter-spacing: 2.5px; }
  .address { top: 276px; font-size: 9.5px; font-weight: 500; letter-spacing: 1px; }
  .postcode { top: 297px; font-size: 7px; font-weight: 600; letter-spacing: 1.5px; }

  .nutrition {
    position: absolute; left: 671px; top: 47px; width: 217px; height: 213px;
    background: var(--panel-white); border-radius: 10px;
    padding: 10px 12px;
    font-family: "Montserrat", Arial, sans-serif; color: var(--bark);
    font-size: 6.5px; line-height: 1.3;
  }
  .nutrition h2 {
    font-size: 10px; font-weight: 500; text-align: center; letter-spacing: 0.3px;
    margin-bottom: 8px;
  }
  .servings { display: flex; justify-content: space-between; padding-bottom: 7px; border-bottom: 0.6px solid var(--rule); }
  .servings ul { list-style: none; }
  .servings li::after {
    content: ""; display: inline-block; width: 4px; height: 4px;
    border: 0.6px solid var(--bark); margin-left: 3px; vertical-align: middle;
  }
  .serving-size { text-align: center; padding-top: 3px; }
  .nutrition-table { width: 100%; border-collapse: collapse; margin-top: 3px; }
  .nutrition-table th { font-weight: 400; text-align: left; font-size: 5.5px; padding-bottom: 4px; border-bottom: 0.6px solid var(--rule); vertical-align: bottom; }
  .nutrition-table td { padding: 4px 0 3px; vertical-align: top; }
  .nutrition-table td:first-child { width: 44%; }
  .best-before {
    position: absolute; right: 50px; top: 276px;
    font-size: 9.5px; font-weight: 700; line-height: 1.05; text-align: right; letter-spacing: 0.3px;
  }
</style>
</head>
<body>
  <main class="label">
    <svg class="label-shapes" viewBox="0 0 936 312">
      <defs>
        <linearGradient id="combTone" x1="0" y1="0" x2="1" y2="1">
          <stop offset="0" stop-color="#fde598"/>
          <stop offset="0.5" stop-color="#fff1c2"/>
          <stop offset="1" stop-color="#fde598"/>
        </linearGradient>
      </defs>
      <polygon class="comb-area comb-left" role="img" aria-label="Honeycomb pattern in pale honey yellow and white" points="0,0 294,0 350,155 301,312 0,312"/>
      <polygon class="panel front-top" points="306,0 633,0 578,144 360,144"/>
      <polygon class="panel front-bottom" points="360,167 578,167 628,312 313,312"/>
      <polygon class="comb-area comb-right" role="img" aria-label="Honeycomb pattern in pale honey yellow and white" points="645,0 936,0 936,312 640,312 590,155"/>
    </svg>

    <p class="center-text net-weight">500g</p>
    <p class="center-text brand-name">BRIGHT MEADOW<br>HONEY</p>
    <p class="center-text product-type">ORGANIC</p>
    <h1 class="center-text product-name">HONEY</h1>
    <p class="center-text company">BRIGHT MEADOW HONEY LTD</p>
    <p class="center-text address">Address line</p>
    <p class="center-text postcode">123ABC</p>

    <section class="nutrition">
      <h2>NUTRITION INFORMATION</h2>
      <div class="servings">
        <ul>
          <li>- Serving per 250g jar: 12.5</li>
          <li>- Serving per 500g jar: 25.0</li>
          <li>- Serving per 1kg jar: 50.0</li>
        </ul>
        <p class="serving-size">SERVING SIZE: 20g<br>(1 Tablespoon)</p>
      </div>
      <table class="nutrition-table">
        <tr><th></th><th>Average<br>quantity<br>Per serving</th><th>Average<br>quantity<br>Per 100g</th></tr>
        <tr><td>Energy</td><td>272 kJ</td><td>1360 kJ</td></tr>
        <tr><td>Protein</td><td>0.08g</td><td>0.4g</td></tr>
        <tr><td>Fat, total<br>- Saturated</td><td>0g<br>0g</td><td>0g<br>0g</td></tr>
        <tr><td>Carbohydrate<br>- Sugars</td><td>15.9g<br>15.6g</td><td>76.9g<br>78.1g</td></tr>
        <tr><td>Sodium</td><td>2.4mg</td><td>12mg</td></tr>
      </table>
    </section>

    <p class="best-before">BEST BEFORE<br>12 May 2020</p>
  </main>
</body>
</html>
```